Neurofeedback Specialist and Sober Living Advocate and Administrator needs a logo design

I need a logo design to capture/demonstrate my work and life's mission:
I provide neurofeedback training services to people from all walks of life, especially for people in recovery from addiction and substance abuse. I am also the administrator for a beautiful sober living home on the beach in Malibu, CA .
Neurofeedback is a brain training exercise that takes advantage of the brain's ability to heal itself, and it speeds up the brain's regeneration process after it has undergone some kind of stress (such as surviving a traumatic brain injury, substance abuse, recovery from mental illness, etc.) I provide neurofeedback sessions privately and at several mental health and substance abuse recovery centers in Malibu and the surrounding areas. I also train other practitioners on how to become neurofeedback providers. I work with adults and children, all ages, with all capability levels, and with a range of needs: from Autism to Peak Performance... Neurofeedback training has been known to decrease anxiety, improve sleep, alleviate symptoms of trauma/PTSD, eliminate symptoms of depression such as fatigue, sadness, motivation issues, improve focus, it can reduce the intensity of chronic pain, help eliminate migraines and seizures, and more. I also provide Neurofeedback to maximize peak performance and am typically the go-to neuroveedback speaiclist in the Malibu, CA area for celebrities such as sports heroes, performers (acting and music), CEO's, etc. I have a new website, brainwavecoveline.example (a work in progress) which features some of the colors I like (such as blue and green) but I also like most other colors except for orange and brown colors, those shades would be the two that I would typically reject.
As the administrator for the sober living home, I help clients get and stay sober as they transition back into their lives... I help guide our clients back into "the real world" after they have completed at least 30 days of treatment at an inpatient rehab or mental health facility. Our sober living website is ClearHarborResidence.example, the colors are blue and white, and our sober living home is considered a boutique business, as we provide personal attention and care, and we can host no more than 10 clients at a time.
Maybe on one side of the card you could have the Neurofeedback Specialist info and on the other side you could have the Sober Living Advocate and Administrator info...

```html
<!DOCTYPE html>
<html lang="en">
<head>
<meta charset="utf-8">
<title>Business cards – Brainwave Coveline &amp; Clear Harbor Residence</title>
<link rel="stylesheet" href="https://fonts.googleapis.com/css2?family=Open+Sans:wght@400;700&display=swap">
<style>
  :root {
    --backdrop: #e9e7e4;
    --card: #ffffff;
    --ink: #4a4f55;
    --teal: #7ecdc8;
    --blue: #3d97d0;
    --slate: #4d5661;
  }
  * { box-sizing: border-box; margin: 0; padding: 0; }
  html, body { width: 1200px; height: 1000px; overflow: hidden; }
  body {
    background: var(--backdrop);
    font-family: "Open Sans", Arial, sans-serif;
    color: var(--ink);
    position: relative;
  }
  .card {
    position: absolute;
    left: 266px;
    width: 666px;
    height: 397px;
    background: var(--card);
    box-shadow: 0 3px 10px rgba(0,0,0,0.18);
  }
  .card--neuro { top: 74px; --accent: var(--teal); }
  .card--sober { top: 533px; --accent: var(--blue); }

  .brand {
    position: absolute;
    top: 112px;
    right: 34px;
    display: flex;
    align-items: center;
    gap: 12px;
    font-weight: 700;
    font-size: 26px;
    letter-spacing: 0.5px;
    text-transform: uppercase;
    color: var(--accent);
  }
  .card--sober .brand { color: var(--slate); }
  .brand__dot {
    width: 22px; height: 22px;
    background: var(--accent);
    border-radius: 50%;
  }
  .card--sober .brand__dot { border-radius: 0; }

  .holder { position: absolute; left: 32px; top: 120px; }
  .holder__name {
    font-weight: 700;
    font-size: 21px;
    color: var(--accent);
    letter-spacing: 0.3px;
    text-transform: uppercase;
    line-height: 26px;
  }
  .holder__role { font-size: 16px; line-height: 20px; }

  .address {
    position: absolute; left: 32px; top: 209px;
    font-size: 16px; line-height: 21px; font-style: normal;
  }
  .contacts {
    position: absolute; left: 32px; top: 258px;
    list-style: none;
    font-size: 16px; line-height: 21.5px;
  }
  .contacts li { display: flex; align-items: center; gap: 7px; }
  .contacts svg { width: 15px; height: 15px; fill: var(--accent); flex: none; }
</style>
</head>
<body>

<section class="card card--neuro">
  <div class="brand"><span class="brand__dot"></span>Brainwave Coveline</div>
  <div class="holder">
    <h1 class="holder__name">Maren Aldridge</h1>
    <p class="holder__role">Trained Specialist</p>
  </div>
  <address class="address">418 Tidewater Ave, #120<br>Harborview CA 90000</address>
  <ul class="contacts">
    <li><svg viewBox="0 0 16 16" aria-hidden="true"><path d="M1 6c0-2 3-3 7-3s7 1 7 3v1h-4V5.5H5V7H1z"/><rect x="3" y="8" width="10" height="6" rx="1"/></svg>+ 000 000 0000</li>
    <li><svg viewBox="0 0 16 16" aria-hidden="true"><rect x="4" y="1" width="8" height="4"/><rect x="1" y="6" width="14" height="6" rx="1"/><rect x="4" y="10" width="8" height="5"/></svg>+ 000 000 0000</li>
    <li><svg viewBox="0 0 16 16" aria-hidden="true"><path d="M1 4h14v9H1z"/><path d="M1 4l7 5 7-5" stroke="#fff" stroke-width="1.3" fill="none"/></svg>info@brainwavecoveline.example</li>
    <li><svg viewBox="0 0 16 16" aria-hidden="true"><circle cx="8" cy="8" r="7"/><path d="M1 8h14M8 1c3 3 3 11 0 14M8 1c-3 3-3 11 0 14" stroke="#fff" stroke-width="1" fill="none"/></svg>www.brainwavecoveline.example</li>
  </ul>
</section>

<section class="card card--sober">
  <div class="brand"><span class="brand__dot"></span>Clear Harbor Residence</div>
  <div class="holder">
    <h2 class="holder__name">Maren Aldridge</h2>
    <p class="holder__role">Trained Specialist</p>
  </div>
  <address class="address">418 Tidewater Ave, #120<br>Harborview CA 90000</address>
  <ul class="contacts">
    <li><svg viewBox="0 0 16 16" aria-hidden="true"><path d="M1 6c0-2 3-3 7-3s7 1 7 3v1h-4V5.5H5V7H1z"/><rect x="3" y="8" width="10" height="6" rx="1"/></svg>+ 000 000 0000</li>
    <li><svg viewBox="0 0 16 16" aria-hidden="true"><rect x="4" y="1" width="8" height="4"/><rect x="1" y="6" width="14" height="6" rx="1"/><rect x="4" y="10" width="8" height="5"/></svg>+ 000 000 0000</li>
    <li><svg viewBox="0 0 16 16" aria-hidden="true"><path d="M1 4h14v9H1z"/><path d="M1 4l7 5 7-5" stroke="#fff" stroke-width="1.3" fill="none"/></svg>info@ClearHarborResidence.example</li>
    <li><svg viewBox="0 0 16 16" aria-hidden="true"><circle cx="8" cy="8" r="7"/><path d="M1 8h14M8 1c3 3 3 11 0 14M8 1c-3 3-3 11 0 14" stroke="#fff" stroke-width="1" fill="none"/></svg>www.ClearHarborResidence.example</li>
  </ul>
</section>

</body>
</html>
```